Bright Reed Yellow Perch Fish Stock and immune system boosts

We are a non-profit that sets up Aquaponics's systems in cities of 5000 or less in the Midwest. We have created a product that uses our yellow perch carcasses as the base for this broth. Our fish are grown in containment from egg to market size fish. This means it is the safest most sustainable product on the market. We also use veggies grown in the same aquaponics system network. One product has oriental overtones and mixed with antioxidants as a gut immune system bacteria booster. The other is a standard broth that has multiple uses. We are looking for packaging for both our broths. We have included our logo (a pixel guild creation). This product packaging will also be a media piece promoting The Bright Reed way of life and a way to raise revenue for the non-profit. We have not chosen the names of products but will be under the "Bright Reed" verbiage. Example is " "Bright Reed Trout Tide stock"
I have added some current examples of packaging

Target Market(s)

consumers and commercial clients

Industry/Entity Type

Grocery Store

Colors

Designer to choose colors to be used in the design.

Requirements
Must have
• Fresh feeling, restorative qualities, safe, sustainable
• Package size is 32 oz. shape is flexible

```html
<!DOCTYPE html>
<html lang="en">
<head>
<meta charset="utf-8">
<title>Bright Reed Cooking Stock – Veggies</title>
<link href="https://fonts.googleapis.com/css2?family=Cinzel:wght@400&family=Noto+Sans:wght@400;500&display=swap" rel="stylesheet">
<style>
  :root {
    --bg: #e9eaeb;
    --carton-white: #f7f7f6;
    --sky-blue: #5eaee0;
    --deep-blue: #1a5c9c;
    --navy: #1e3f7a;
    --lime: #8dc63f;
    --ink: #2b2b2b;
    --photo-dark: #3a3f44;
    --photo-mid: #8a8a80;
    --photo-light: #cfd3c4;
  }
  * { margin: 0; padding: 0; box-sizing: border-box; }
  html, body { width: 1200px; height: 900px; overflow: hidden; background: var(--bg); }
  .canvas { position: relative; width: 1200px; height: 900px; }
  .carton-front {
    position: absolute; left: 395px; top: 35px; width: 410px; height: 830px;
    background: var(--carton-white); overflow: hidden;
    font-family: "Noto Sans", sans-serif;
  }
  .carton-shapes { position: absolute; inset: 0; }
  .brand { position: absolute; top: 112px; left: 0; width: 100%; text-align: center; }
  .brand-dot { width: 70px; height: 70px; border-radius: 50%; background: var(--deep-blue); margin: 0 auto 12px; }
  .brand-name { font-family: "Cinzel", serif; font-size: 22px; color: var(--ink); letter-spacing: 0.5px; line-height: 1; }
  .brand-region { font-family: "Cinzel", serif; font-size: 11.5px; color: var(--ink); margin-top: 4px; }
  .product { position: absolute; top: 290px; left: 0; width: 100%; text-align: center; }
  .product-title { font-size: 46px; font-weight: 500; color: var(--deep-blue); line-height: 0.95; letter-spacing: -0.5px; }
  .product-flavour {
    display: inline-block; margin-top: 6px; width: 190px; height: 36px; line-height: 36px;
    border-radius: 18px; background: var(--lime); color: #fff; font-size: 32px; letter-spacing: -0.5px;
  }
  .product-claim { font-size: 22px; color: var(--navy); margin-top: 2px; word-spacing: 10px; }
  .nutrition { position: absolute; top: 754px; left: 145px; display: flex; gap: 4px; }
  .nutrition-box {
    width: 33px; height: 56px; background: var(--navy); border: 1px solid #8fb3d8; border-radius: 3px;
    color: #fff; text-align: center;
  }
  .nutrition-box .value { font-size: 20px; line-height: 28px; border-bottom: 1px solid #fff; margin: 0 3px; }
  .nutrition-box .value.small { font-size: 12px; }
  .nutrition-box .label { font-size: 7.5px; margin-top: 3px; }
  .net-weight {
    position: absolute; top: 813px; left: 135px; width: 140px; height: 14px; line-height: 14px;
    border-radius: 7px; background: var(--navy); border: 1px solid #8fb3d8;
    color: #fff; font-size: 8px; text-align: center;
  }
</style>
</head>
<body>
<div class="canvas">
  <section class="carton-front">
    <svg class="carton-shapes" width="410" height="830" viewBox="0 0 410 830">
      <defs>
        <radialGradient id="stockPhoto" cx="50%" cy="55%" r="60%">
          <stop offset="0" stop-color="var(--photo-light)"/>
          <stop offset="0.6" stop-color="var(--photo-mid)"/>
          <stop offset="1" stop-color="var(--photo-dark)"/>
        </radialGradient>
      </defs>
      <path class="top-band" d="M0 0 H410 V112 C370 112 350 100 330 70 C312 40 300 28 282 28 H128 C110 28 98 40 80 70 C60 100 40 112 0 112 Z" fill="var(--sky-blue)"/>
      <path d="M0 112 C40 112 60 100 80 70 C98 40 110 28 128 28" fill="none" stroke="var(--navy)" stroke-width="2"/>
      <path d="M410 112 C370 112 350 100 330 70 C312 40 300 28 282 28" fill="none" stroke="var(--navy)" stroke-width="2"/>
      <path class="photo-area" role="img" aria-label="Photo of a steaming pot of vegetable broth with mushrooms, cabbage, leeks and carrots"
            d="M0 600 C20 540 100 500 210 500 C320 500 395 540 410 590 V830 H0 Z" fill="url(#stockPhoto)"/>
      <path class="bottom-wave-left" d="M0 690 C40 700 60 730 65 780 C68 810 90 828 120 830 H0 Z" fill="var(--sky-blue)"/>
      <path d="M0 690 C40 700 60 730 65 780 C68 810 90 828 120 830" fill="none" stroke="var(--navy)" stroke-width="2"/>
      <path class="bottom-wave-right" d="M410 640 C360 650 330 700 335 760 C338 800 320 825 290 830 H410 Z" fill="var(--sky-blue)"/>
      <path d="M410 640 C360 650 330 700 335 760 C338 800 320 825 290 830" fill="none" stroke="var(--navy)" stroke-width="2"/>
    </svg>

    <div class="brand">
      <div class="brand-dot"></div>
      <div class="brand-name">Bright Reed</div>
      <div class="brand-region">Great Lakes Region</div>
    </div>

    <div class="product">
      <h1 class="product-title">COOKING<br>STOCK</h1>
      <div class="product-flavour">VEGGIES</div>
      <div class="product-claim">100% NATURAL</div>
    </div>

    <div class="nutrition">
      <div class="nutrition-box"><div class="value">15</div><div class="label">Calories</div></div>
      <div class="nutrition-box"><div class="value">0</div><div class="label">Salt Fat</div></div>
      <div class="nutrition-box"><div class="value small">550g</div><div class="label">Sodium</div></div>
      <div class="nutrition-box"><div class="value">2</div><div class="label">Sugar</div></div>
    </div>
    <div class="net-weight">NET WT: 32 Oz (213) (907G)</div>
  </section>
</div>
</body>
</html>
```